Artificial intelligence, machine learning, and automation company needs a sexy business card design

We need a sleek and sexy business card design for an AI consulting company based in Philadelphia PA. We provide custom machine learning and automation solutions for companies of all shapes and sizes. The primary industries that we serve are pharmaceuticals, engineering, healthcare, and computer software. We would like the designs to be a black business card that uses green as a sleek accent color. The final design should communicate intelligence, cutting edge new-tech, and optimization.

Target Market(s)

C-level and VP level executives of multi-million annual companies. Mostly in Pharma, Healthcare, Real Estate, Retail, and Engineering

Industry/Entity Type

Computer Software

Contact Information for Business Card

Name: Jack Moss
Title: CEO
Cell: 215 604 8293
Email: JackM@quillarcworks.example
Website: www.QuillarcWorks.example

Font styles to use
Sans Serif

Colors

Designer to choose colors to be used in the design.

Requirements
Must have
• 1) Attached Quillarc Logo (either with colors or not/embossed)
• 2) "Artificial Intelligence" "Automation" and "Machine Learning"
• 3) "Quillarc Laboratories" or "Quillarc Works" or "Quillarc"
• 4) Sexy AF.
Nice to have
• Black card / dark card color, "Quillarc Green" accent colors (in attached .ai file), Embossment of logo/name/etc, thick card stock, colored borders (on card sides, not front/back faces)
Should not have
• Should not be bland, or unsexy.

```html
<!DOCTYPE html>
<html lang="en">
<head>
<meta charset="utf-8">
<title>Quillarc Laboratories — Business Card</title>
<link href="https://fonts.googleapis.com/css2?family=Roboto:wght@300;400;500;700&display=swap" rel="stylesheet">
<style>
  :root {
    --page-bg: #2b2e33;
    --card-black: #121212;
    --card-edge: #0a0a0a;
    --text-white: #f2f2f2;
    --text-soft: #d6d6d6;
    --quillarc-green: #3fb8a5;
  }
  * { margin: 0; padding: 0; box-sizing: border-box; }
  html, body {
    width: 1200px; height: 900px; overflow: hidden;
    background: var(--page-bg);
    font-family: "Roboto", Arial, sans-serif;
  }
  .canvas {
    position: relative; width: 1200px; height: 900px;
  }
  .card {
    position: absolute; left: 320px; width: 560px; height: 320px;
    background: var(--card-black);
    border-radius: 22px;
    box-shadow: 0 6px 0 var(--card-edge), 0 18px 40px rgba(0,0,0,0.45);
    color: var(--text-white);
  }
  .card--back { top: 70px; }
  .card--front { top: 490px; }

  /* Back face */
  .brand {
    position: absolute; left: 0; right: 0; top: 112px;
    display: flex; align-items: center; justify-content: center; gap: 22px;
  }
  .brand__square {
    width: 62px; height: 62px;
    border: 4px solid var(--quillarc-green);
  }
  .brand__name {
    font-size: 25px; font-weight: 400; letter-spacing: 5px;
    text-transform: uppercase; color: var(--text-white);
  }
  .back-website {
    position: absolute; left: 0; right: 0; top: 232px;
    text-align: center; font-size: 14px; color: var(--text-white);
    letter-spacing: 0.3px;
  }
  .back-website .accent { color: var(--quillarc-green); }

  /* Front face */
  .identity {
    position: absolute; left: 40px; top: 88px; width: 210px;
    text-align: right;
  }
  .identity__name {
    font-size: 34px; line-height: 1; letter-spacing: 0.5px;
  }
  .identity__first { font-weight: 300; color: var(--text-white); }
  .identity__last { font-weight: 700; color: var(--quillarc-green); }
  .identity__title {
    margin-top: 6px; font-size: 20px; font-weight: 300; color: var(--text-white);
  }
  .divider {
    position: absolute; left: 272px; top: 80px; width: 2px; height: 96px;
    background: var(--quillarc-green);
  }
  .contacts {
    position: absolute; left: 292px; top: 86px;
    list-style: none; font-size: 15px; color: var(--text-white);
  }
  .contacts li {
    display: flex; align-items: center; gap: 10px; height: 28px;
  }
  .contacts svg { width: 16px; height: 16px; flex: none; }
  .services {
    position: absolute; left: 0; right: 0; bottom: 42px;
    display: flex; justify-content: center; align-items: center; gap: 16px;
    font-size: 15px; color: var(--text-soft);
  }
  .services__sep { width: 2px; height: 16px; background: var(--quillarc-green); }
</style>
</head>
<body>
<main class="canvas">

  <section class="card card--back" aria-label="Card back">
    <div class="brand">
      <span class="brand__square" aria-hidden="true"></span>
      <span class="brand__name">Quillarc Laboratories</span>
    </div>
    <p class="back-website">www.<span class="accent">quillarcworks</span>.example</p>
  </section>

  <section class="card card--front" aria-label="Card front">
    <div class="identity">
      <p class="identity__name"><span class="identity__first">JACK</span> <span class="identity__last">MOSS</span></p>
      <p class="identity__title">CEO</p>
    </div>
    <span class="divider" aria-hidden="true"></span>
    <ul class="contacts">
      <li>
        <svg viewBox="0 0 16 16" aria-hidden="true"><rect x="4" y="1" width="8" height="14" rx="1.5" fill="none" stroke="#3fb8a5" stroke-width="1.5"/><line x1="7" y1="12.5" x2="9" y2="12.5" stroke="#3fb8a5" stroke-width="1.5"/></svg>
        <span>215 604 8293</span>
      </li>
      <li>
        <svg viewBox="0 0 16 16" aria-hidden="true"><rect x="1" y="3" width="14" height="10" fill="none" stroke="#3fb8a5" stroke-width="1.5"/><polyline points="1,3 8,9 15,3" fill="none" stroke="#3fb8a5" stroke-width="1.5"/></svg>
        <span>JackM@quillarcworks.example</span>
      </li>
      <li>
        <svg viewBox="0 0 16 16" aria-hidden="true"><circle cx="8" cy="8" r="7" fill="#3fb8a5"/><g stroke="#121212" stroke-width="1" fill="none"><ellipse cx="8" cy="8" rx="3" ry="7"/><line x1="1" y1="8" x2="15" y2="8"/><line x1="2" y1="4.5" x2="14" y2="4.5"/><line x1="2" y1="11.5" x2="14" y2="11.5"/></g></svg>
        <span>www.quillarcworks.example</span>
      </li>
    </ul>
    <p class="services">
      <span>Artificial Intelligence</span>
      <span class="services__sep" aria-hidden="true"></span>
      <span>Automation</span>
      <span class="services__sep" aria-hidden="true"></span>
      <span>Machine Learning</span>
    </p>
  </section>

</main>
</body>
</html>
```